I need a wordpress website for myconsulting company specialized in data privacy

I'm looking for a wordpress website for my consulting company specialized in data privacy (GDPR) and computer science.
The website will serve as entry point to for potential clients.
The website should have the following sections (I'm opened to new ideas):
- Presentation of the company
- General presentation
- Services provided with some details
- Blog/articles with tags (if possible)
- Contact
On every page of the website there should be some references to pages (such as privacy policy, legal information...)
If possible he website should be multinlingual (english and french). I'll personnally take care of the translation in french.
Regarding branding;
- Name of the company: Laurent Dubreuil Conseil
- Logo is attached
- For colors to be used see attached PDF for exemple

```html
<!DOCTYPE html>
<html lang="en">
<head>
<meta charset="utf-8">
<title>Laurent Dubreuil Conseil — Data privacy &amp; Computer Science</title>
<link rel="stylesheet" href="https://fonts.googleapis.com/css2?family=Michroma&family=Urbanist:wght@400;500;600&family=Barlow+Condensed:wght@500;600&display=swap">
<style>
:root{
  --teal:#0e8896;
  --teal-dark:#0a6f7c;
  --cyan:#0cc4dc;
  --navy:#031a29;
  --mist:#e8ebf4;
  --ink:#0b1b2a;
  --body:#3c4652;
  --white:#ffffff;
  --green:#3fbf6f;
}
*{margin:0;padding:0;box-sizing:border-box}
html,body{width:1200px;height:3825px;overflow:hidden}
body{position:relative;background:var(--white);font-family:"Urbanist",sans-serif;color:var(--body)}
.abs{position:absolute}
.display{font-family:"Michroma",sans-serif;color:var(--ink);letter-spacing:1px}
.cond{font-family:"Barlow Condensed",sans-serif}
.btn{position:absolute;display:flex;align-items:center;justify-content:center;background:var(--teal);color:var(--white);font-family:"Barlow Condensed",sans-serif;font-weight:600;font-size:16px;border-radius:3px}
.shape{position:absolute;left:0;top:0}
.media{position:absolute}

/* hero */
.hero-bg{left:0;top:0;width:1200px;height:600px;background:linear-gradient(180deg,#eef0f7,#e4e8f2)}
.brand{display:flex;align-items:center;gap:10px}
.brand-square{width:26px;height:26px;background:var(--teal);border-radius:3px}
.brand-name{font-family:"Urbanist",sans-serif;font-weight:600;font-size:16px;color:var(--navy)}
.nav{left:514px;top:26px;display:flex;gap:46px;font-family:"Barlow Condensed",sans-serif;font-weight:500;font-size:15px;color:var(--ink)}
.nav .active{color:var(--teal);border-bottom:2px solid var(--teal);padding-bottom:4px}
.nav .phone{color:var(--teal);display:flex;gap:6px;align-items:center}
.kicker{font-family:"Michroma",sans-serif;color:var(--teal);font-size:19px;font-style:normal}
.hero-title{left:163px;top:234px;font-size:32px;line-height:45px}
.slider{left:163px;top:503px;display:flex;align-items:center;gap:6px;font-family:"Barlow Condensed",sans-serif;font-size:14px;color:var(--teal)}
.slider .bar{width:145px;height:1px;background:var(--teal)}
.slider .end{color:var(--ink);font-size:11px}

/* welcome */
.welcome-text{left:608px;top:634px;width:430px}
.welcome-text h2{font-size:32px;line-height:40px;margin-top:6px}
.welcome-text p{font-size:14.5px;line-height:22.5px;margin-top:22px;color:var(--body)}

/* why */
.why{left:163px;top:1140px;width:460px;color:#dfe7ee}
.why h2{font-family:"Michroma",sans-serif;color:var(--white);font-size:32px;letter-spacing:1px}
.why p{font-size:15px;line-height:22px;margin-top:18px}
.why ul{list-style:none;margin-top:18px}
.why li{display:flex;align-items:center;gap:10px;font-size:15px;margin-bottom:9px;color:var(--white)}

/* services */
.section-title{width:1200px;text-align:center;font-family:"Michroma",sans-serif;font-size:32px;letter-spacing:2px}
.section-title .light{color:var(--teal);font-weight:400}
.service{position:absolute;top:1630px;width:267px;height:392px;text-align:center}
.service h3{position:absolute;top:148px;width:100%;font-family:"Barlow Condensed",sans-serif;font-weight:500;font-size:25px;color:var(--ink)}
.service p{position:absolute;top:195px;left:30px;width:207px;font-size:16px;line-height:25px;color:var(--body)}
.service .more{position:absolute;top:330px;width:100%;font-family:"Barlow Condensed",sans-serif;font-weight:600;font-size:16px;color:var(--teal)}
.outline-btn{left:525px;top:2041px;width:150px;height:44px;border:2px solid var(--teal);border-radius:3px;display:flex;align-items:center;justify-content:center;font-family:"Barlow Condensed",sans-serif;font-weight:600;font-size:16px;color:var(--teal)}

/* blog */
.post{position:absolute;top:2318px;width:278px}
.post .thumb{width:278px;height:190px;border-radius:10px}
.post .date{margin-top:10px;font-family:"Barlow Condensed",sans-serif;font-size:13px;color:var(--cyan)}
.post h3{margin-top:6px;font-family:"Barlow Condensed",sans-serif;font-weight:500;font-size:22px;color:var(--white)}
.post p{margin-top:6px;font-size:15px;line-height:22px;color:#dce5ec}
.post .more{margin-top:10px;display:flex;align-items:center;gap:8px;font-family:"Barlow Condensed",sans-serif;font-size:15px;color:var(--cyan)}

/* contact */
.message-card{left:163px;top:2835px;width:655px;height:420px;background:var(--white);border-radius:16px}
.message-card h2{position:absolute;left:32px;top:42px;font-size:25px;line-height:34px}
.field{position:absolute;left:34px;width:476px;border-bottom:1px solid #9aa3ad;font-size:13px;color:var(--ink)}
.contact-card{left:712px;top:2898px;width:324px;height:407px;background:var(--teal);border-radius:16px;color:var(--white)}
.contact-card h2{position:absolute;left:20px;top:62px;font-family:"Michroma",sans-serif;font-size:24px;letter-spacing:1px}
.contact-card .lead{position:absolute;left:20px;top:100px;width:290px;font-size:15px;line-height:22px}
.info{position:absolute;left:20px;display:flex;gap:12px;font-size:15px;line-height:22px}
.pill{position:absolute;height:12px;border-radius:6px}

/* footer */
.footer{left:0;top:3355px;width:1200px;height:470px;background:var(--navy);text-align:center;color:#c8d3dd}
.footer h2{margin-top:80px;font-family:"Michroma",sans-serif;color:var(--white);font-size:26px;letter-spacing:2px}
.footer .lead{margin:8px auto 0;width:600px;font-size:15px;line-height:22px}
.subscribe{position:absolute;left:385px;top:175px;width:432px;height:52px;background:var(--white);border-radius:6px;display:flex;align-items:center;justify-content:space-between;padding:0 4px 0 18px;font-size:13px;color:#6d7781}
.subscribe .go{width:120px;height:44px;background:var(--teal);color:var(--white);border-radius:4px;display:flex;align-items:center;justify-content:center;font-family:"Barlow Condensed",sans-serif;font-weight:600;font-size:16px}
.footer .brand{position:absolute;left:0;width:1200px;top:266px;justify-content:center}
.footer .brand-name{color:var(--white)}
.footer-nav{position:absolute;top:368px;left:0;width:1200px;display:flex;justify-content:center;gap:48px;font-family:"Barlow Condensed",sans-serif;font-weight:600;font-size:16px;color:var(--white)}
.footer-rule{position:absolute;left:163px;top:405px;width:873px;height:1px;background:#23384a}
.copy{position:absolute;top:428px;width:1200px;font-family:"Barlow Condensed",sans-serif;font-size:14px}
.copy span{color:var(--cyan)}
</style>
</head>
<body>

<!-- HERO -->
<div class="abs hero-bg"></div>
<svg class="shape" width="1200" height="620" viewBox="0 0 1200 620">
  <polygon points="0,0 480,0 408,84 0,84" fill="#ffffff"/>
  <polyline points="0,88 410,88 486,2 1200,2" fill="none" stroke="var(--teal)" stroke-width="5"/>
  <polygon points="0,605 580,605 690,518 1200,518 1200,620 0,620" fill="#ffffff"/>
  <polyline points="0,603 580,603 688,514 1200,514" fill="none" stroke="var(--teal)" stroke-width="5"/>
</svg>
<div class="abs brand" style="left:163px;top:28px"><div class="brand-square"></div><div class="brand-name">Laurent Dubreuil Conseil</div></div>
<nav class="abs nav">
  <span class="active">Home</span><span>About</span><span>Services</span><span>Blog</span><span>Contact</span>
  <span class="phone"><svg width="13" height="13" viewBox="0 0 24 24"><path d="M6.6 10.8a15 15 0 0 0 6.6 6.6l2.2-2.2a1 1 0 0 1 1-.25 11 11 0 0 0 3.6.6 1 1 0 0 1 1 1V20a1 1 0 0 1-1 1A17 17 0 0 1 3 4a1 1 0 0 1 1-1h3.5a1 1 0 0 1 1 1 11 11 0 0 0 .6 3.6 1 1 0 0 1-.25 1z" fill="var(--teal)"/></svg>01 234 567 890</span>
</nav>
<div class="abs kicker" style="left:163px;top:208px">We Specialized in</div>
<h1 class="abs display hero-title">Data privacy &amp;<br>Computer Science</h1>
<div class="btn" style="left:163px;top:340px;width:150px;height:44px">Learn More</div>
<div class="abs slider">01<div class="bar"></div><span class="end">04</span></div>
<div class="media" role="img" aria-label="Isometric illustration of a desktop monitor with a profile card, a red padlock, a key, a smartphone and floating cubes" style="left:640px;top:50px;width:545px;height:440px;border-radius:40px;background:radial-gradient(circle at 55% 40%,#c6b6ff 0%,#a7c9f4 35%,#dfe3f2 70%,rgba(232,235,244,0) 100%)"></div>

<!-- WELCOME -->
<div class="media" role="img" aria-label="Photo of a man working at a computer keyboard in front of a teal frame" style="left:163px;top:628px;width:402px;height:318px;border-radius:30px;background:linear-gradient(135deg,#2e8f9d,#4aa9b6 50%,#6c7780)"></div>
<div class="abs welcome-text">
  <div class="kicker">Welcome to</div>
  <h2 class="display">Laurent Dubreuil<br>Conseil</h2>
  <p>Nulla rhoncus scelerisque urna at sagittis. Nam non justo sit amet eros laoreet maximus sit amet et felis. Nullam id enim consequat, pharetra ligula non, falisis ligula. Sed et iaculis massa, vel elemtum nulla. Sed in magna fringilla molestie. Sed vehicula vel elit sit amet hendrerit. In sollicitudin, eros in tempor ullamcorper, tortor mauris tempor eros,</p>
</div>
<div class="btn" style="left:608px;top:908px;width:150px;height:42px">Read More</div>

<!-- WHY CHOOSE US -->
<svg class="shape" style="top:990px" width="1200" height="530" viewBox="0 0 1200 530">
  <polygon points="0,82 570,82 682,20 1200,20 1200,440 682,440 570,522 0,522" fill="var(--navy)"/>
  <polyline points="0,74 560,74 670,4 1200,4" fill="none" stroke="var(--teal)" stroke-width="5"/>
  <polyline points="0,520 556,520 670,450 1200,450" fill="none" stroke="var(--teal)" stroke-width="5"/>
</svg>
<div class="abs why">
  <h2>Why Choose Us</h2>
  <p>Lorem ipsum dolor sit amet, consectetur adipiscing elit. Nullam pulvinar odio diam, efficitur convallis nulla ornare rutrum.</p>
  <ul>
    <li><svg width="16" height="14" viewBox="0 0 16 14"><path d="M1 7l5 5 9-11" fill="none" stroke="var(--green)" stroke-width="3"/></svg>Lorem ipsum dolor sit amet, consectetur</li>
    <li><svg width="16" height="14" viewBox="0 0 16 14"><path d="M1 7l5 5 9-11" fill="none" stroke="var(--green)" stroke-width="3"/></svg>Quis ipsum suspendisse ultrices gravida.</li>
    <li><svg width="16" height="14" viewBox="0 0 16 14"><path d="M1 7l5 5 9-11" fill="none" stroke="var(--green)" stroke-width="3"/></svg>Risus commodo viverra maecenas</li>
  </ul>
</div>
<div class="btn" style="left:163px;top:1369px;width:150px;height:42px">Read More</div>
<div class="media" role="img" aria-label="Photo of a person at a desk facing a monitor showing a privacy shield message" style="left:665px;top:1060px;width:370px;height:355px;border-radius:30px;background:linear-gradient(160deg,#d9dfe0,#6d8a90 45%,#1f5a66 75%,#0e8896)"></div>

<!-- SERVICES -->
<h2 class="abs section-title display" style="top:1555px"><span class="light">Our</span> Services</h2>

<div class="service" style="left:159px">
  <svg class="shape" width="267" height="392" viewBox="0 0 267 392"><path d="M4 190V133A129.5 129.5 0 0 1 263 133V190" fill="none" stroke="var(--cyan)" stroke-width="8"/><path d="M4 268V259A129.5 129.5 0 0 0 263 259V268" fill="none" stroke="var(--cyan)" stroke-width="8"/><circle cx="133.5" cy="84" r="50" fill="var(--cyan)"/><path d="M133.5 60l18 7v13c0 12-8 20-18 24-10-4-18-12-18-24V67z" fill="#ffffff"/><rect x="126" y="80" width="15" height="11" rx="2" fill="var(--teal)"/></svg>
  <h3>Security Services</h3>
  <p>Lorem ipsum dolor sit amet, consecr adipiscing elit, sed do eiusmod tr incididunt ut labore et dolore magna aliqua.</p>
  <div class="more">Read More +</div>
</div>
<div class="service" style="left:464px">
  <svg class="shape" width="267" height="392" viewBox="0 0 267 392"><path d="M4 190V133A129.5 129.5 0 0 1 263 133V190" fill="none" stroke="#08aecb" stroke-width="8"/><path d="M4 268V259A129.5 129.5 0 0 0 263 259V268" fill="none" stroke="#08aecb" stroke-width="8"/><circle cx="133.5" cy="84" r="50" fill="#08aecb"/><rect x="116" y="64" width="30" height="38" rx="3" fill="#ffffff"/><path d="M121 74h20M121 82h20M121 90h14" stroke="#08aecb" stroke-width="2"/><circle cx="146" cy="66" r="9" fill="#f4c21b"/></svg>
  <h3>Data Privacy</h3>
  <p>Lorem ipsum dolor sit amet, consecr adipiscing elit, sed do eiusmod tr incididunt ut labore et dolore magna aliqua.</p>
  <div class="more">Read More +</div>
</div>
<div class="service" style="left:767px">
  <svg class="shape" width="267" height="392" viewBox="0 0 267 392"><path d="M4 190V133A129.5 129.5 0 0 1 263 133V190" fill="none" stroke="var(--teal)" stroke-width="8"/><path d="M4 268V259A129.5 129.5 0 0 0 263 259V268" fill="none" stroke="var(--teal)" stroke-width="8"/><circle cx="133.5" cy="84" r="50" fill="var(--teal)"/><rect x="112" y="66" width="36" height="26" rx="3" fill="#ffffff"/><rect x="127" y="92" width="6" height="7" fill="#ffffff"/><rect x="120" y="99" width="20" height="3" fill="#ffffff"/><rect x="150" y="70" width="4" height="18" fill="#e05a8a"/></svg>
  <h3>Computer Sicence</h3>
  <p>Lorem ipsum dolor sit amet, consecr adipiscing elit, sed do eiusmod tr incididunt ut labore et dolore magna aliqua.</p>
  <div class="more">Read More +</div>
</div>
<div class="abs outline-btn">View All Services</div>

<!-- BLOG -->
<svg class="shape" style="top:2120px" width="1200" height="650" viewBox="0 0 1200 650">
  <polygon points="0,108 560,108 680,24 1200,24 1200,548 680,548 560,636 0,636" fill="var(--navy)"/>
  <polyline points="0,100 556,100 672,10 1200,10" fill="none" stroke="var(--teal)" stroke-width="5"/>
  <polyline points="0,634 556,634 672,544 1200,544" fill="none" stroke="var(--teal)" stroke-width="5"/>
</svg>
<h2 class="abs section-title" style="top:2253px;color:#ffffff;font-family:'Michroma',sans-serif;letter-spacing:2px"><span style="color:var(--teal)">Blog</span> &amp; Articles</h2>
<svg class="abs" style="left:133px;top:2402px" width="36" height="26" viewBox="0 0 36 26"><path d="M35 13H2M13 2L2 13l11 11" fill="none" stroke="#ffffff" stroke-width="2"/></svg>
<svg class="abs" style="left:1031px;top:2402px" width="36" height="26" viewBox="0 0 36 26"><path d="M1 13h33M23 2l11 11-11 11" fill="none" stroke="var(--cyan)" stroke-width="2"/></svg>

<article class="post" style="left:163px">
  <div class="thumb" role="img" aria-label="Photo of two people working at computers showing green code" style="background:linear-gradient(135deg,#3c4a4a,#5f8f72 45%,#2b3034)"></div>
  <div class="date">Feb 16, 2022</div>
  <h3>Nam condimentum pharetra</h3>
  <p>Lorem ipsum dolor sit amet, conctetur adipiscing elit, sed do eiusmod</p>
  <div class="more">Read More <svg width="16" height="8" viewBox="0 0 16 8"><path d="M0 4h15M11 1l4 3-4 3" fill="none" stroke="var(--cyan)"/></svg></div>
</article>
<article class="post" style="left:460px">
  <div class="thumb" role="img" aria-label="Photo of a developer typing at a keyboard in front of code screens" style="background:linear-gradient(135deg,#c9d2da,#6b7a88 45%,#1e2a36)"></div>
  <div class="date">Feb 16, 2022</div>
  <h3>Nam condimentum pharetra</h3>
  <p>Lorem ipsum dolor sit amet, conctetur adipiscing elit, sed do eiusmod</p>
  <div class="more">Read More <svg width="16" height="8" viewBox="0 0 16 8"><path d="M0 4h15M11 1l4 3-4 3" fill="none" stroke="var(--cyan)"/></svg></div>
</article>
<article class="post" style="left:757px">
  <div class="thumb" role="img" aria-label="Photo of a woman using a laptop at a bright desk" style="background:linear-gradient(135deg,#f1ece6,#c7b8a9 50%,#5d6a74)"></div>
  <div class="date">Feb 16, 2022</div>
  <h3>Nam condimentum pharetra</h3>
  <p>Lorem ipsum dolor sit amet, conctetur adipiscing elit, sed do eiusmod</p>
  <div class="more">Read More <svg width="16" height="8" viewBox="0 0 16 8"><path d="M0 4h15M11 1l4 3-4 3" fill="none" stroke="var(--cyan)"/></svg></div>
</article>

<!-- CONTACT -->
<div class="abs" style="left:0;top:2758px;width:1200px;height:597px;background:var(--mist);z-index:-1"></div>
<div class="pill" style="left:140px;top:3198px;width:35px;background:#ffffff"></div>
<div class="pill" style="left:112px;top:3218px;width:60px;background:#ffffff"></div>
<div class="abs message-card">
  <h2 class="display">Send us A<br>Message</h2>
  <div class="field" style="top:140px;padding-bottom:6px">Name</div>
  <div class="field" style="top:196px;padding-bottom:6px">Email</div>
  <div class="field" style="top:244px;height:92px">Message</div>
  <div class="btn" style="left:380px;top:340px;width:136px;height:44px">Send To Us</div>
</div>
<div class="pill" style="left:1020px;top:2943px;width:42px;background:var(--teal)"></div>
<div class="pill" style="left:1030px;top:2962px;width:30px;background:var(--teal)"></div>
<div class="pill" style="left:1020px;top:3238px;width:30px;background:var(--teal)"></div>
<div class="pill" style="left:1030px;top:3257px;width:36px;background:var(--teal)"></div>
<div class="abs contact-card">
  <h2>Contact Us</h2>
  <p class="lead">Pellentesque habitant morbi tristique senectus et netus et malesuada</p>
  <div class="info" style="top:162px"><svg width="14" height="18" viewBox="0 0 14 18"><path d="M7 0a7 7 0 0 1 7 7c0 5-7 11-7 11S0 12 0 7a7 7 0 0 1 7-7z" fill="#ffffff"/><circle cx="7" cy="7" r="2.5" fill="var(--teal)"/></svg><span>18 Rue des Tilleuls, Lyon,<br>France</span></div>
  <div class="info" style="top:226px"><svg width="16" height="18" viewBox="0 0 16 18"><rect x="0" y="5" width="16" height="11" rx="1" fill="#ffffff"/><path d="M0 6l8 5 8-5" fill="none" stroke="var(--teal)" stroke-width="1.5"/></svg><span>hello@dubreuil-conseil.example</span></div>
  <div class="info" style="top:264px"><svg width="16" height="18" viewBox="0 0 24 24"><path d="M6.6 10.8a15 15 0 0 0 6.6 6.6l2.2-2.2a1 1 0 0 1 1-.25 11 11 0 0 0 3.6.6 1 1 0 0 1 1 1V20a1 1 0 0 1-1 1A17 17 0 0 1 3 4a1 1 0 0 1 1-1h3.5a1 1 0 0 1 1 1 11 11 0 0 0 .6 3.6 1 1 0 0 1-.25 1z" fill="#ffffff"/></svg><span>01 234 567 890</span></div>
  <div class="abs" style="left:28px;top:316px;display:flex;gap:14px">
    <span style="width:10px;height:10px;border-radius:50%;background:#ffffff"></span>
    <span style="width:10px;height:10px;border-radius:50%;background:#ffffff"></span>
    <span style="width:10px;height:10px;border-radius:50%;background:#ffffff"></span>
  </div>
</div>

<!-- NEWSLETTER & FOOTER -->
<footer class="abs footer">
  <h2>Subscribe Our Newsletter</h2>
  <p class="lead">Lorem ipsum dolor sit amet, consectetur adipiscing elit. Mauris augunibh, viverra et enim ut, facilisis dapibus massa. pulvinar a</p>
  <div class="subscribe"><span>Enter Email Address</span><span class="go">Subscribe</span></div>
  <div class="brand"><div class="brand-square"></div><div class="brand-name">Laurent Dubreuil Conseil</div></div>
  <nav class="footer-nav"><span>Home</span><span>About</span><span>Services</span><span>Blog</span><span>Contact</span></nav>
  <div class="footer-rule"></div>
  <div class="copy">© 2022 <span>Laurent Dubreuil Conseil</span>. All right reserved</div>
</footer>

</body>
</html>
```